Birchway Appliance Care - Repair Plan Paperwork

Home Appliance Repair Agent and Repair Plan providing services to consumers' home appliances.

Pages Layout Guideline:
1) Introduction to BAC / Plan Schedule / Repair Plan Ref
2) Appliance Type / Model / Age / Cost of appliance within Repair Plan / Payment Schedule / Payment Dates / Amounts
3) Terms & Conditions

- Will also want a flyer design to go inside with the paperwork to market savings by adding additional products.

I have uploaded the logo, letterheads and website pages so you get a feel of the branding / design we use throughout.

```html
<!DOCTYPE html>
<html lang="en">
<head>
<meta charset="utf-8">
<title>Birchway Appliance Care – Repair Plan Paperwork</title>
<link href="https://fonts.googleapis.com/css2?family=Montserrat:wght@400;500;600;700&display=swap" rel="stylesheet">
<style>
:root{
  --teal:#1fb0c3;
  --orange:#f15a2b;
  --dark:#3b3c41;
  --ink:#2a2a2e;
  --paper:#ffffff;
  --marble:#f6f7f8;
  --stage:#d9dce2;
}
*{box-sizing:border-box;margin:0;padding:0}
html,body{width:1200px;height:1040px;overflow:hidden;background:var(--stage);font-family:'Montserrat',sans-serif;color:var(--ink)}
.page{position:absolute;top:258px;width:370px;height:523px;background:var(--paper);overflow:hidden;box-shadow:0 4px 14px rgba(0,0,0,.18)}
.page--intro{left:20px}
.page--appliances{left:415px}
.page--booking{left:810px;background:linear-gradient(135deg,#fff 0%,var(--marble) 50%,#fff 100%)}
.abs{position:absolute}
.body-text{font-size:5.6px;line-height:1.45;text-align:justify}
.body-text p+p{margin-top:5px}
.heading{font-weight:600;letter-spacing:.2px}
.heading--teal{color:var(--teal)}
.heading--orange{color:var(--orange)}

/* footer */
.footer{position:absolute;left:0;bottom:0;width:370px;height:130px}
.footer-photo{position:absolute;left:252px;top:420px;width:150px;height:150px;border-radius:50%;border:3px solid var(--orange);background:linear-gradient(160deg,#e9e6e1 0%,#bcb5ad 45%,#6d6761 100%)}
.footer-contact{position:absolute;left:120px;top:472px;color:#fff;font-size:5.8px;line-height:1.35}
.footer-contact p+p{margin-top:3px}

/* page 1 */
.hero-art{position:absolute;left:0;top:0;width:370px;height:260px}
.brand{position:absolute;left:24px;top:20px;color:#fff;font-weight:500}
.brand-name{font-size:27px;letter-spacing:1px;line-height:1}
.brand-tag{font-size:8.6px;letter-spacing:2.6px;margin-top:2px;padding-left:14px}
.intro-col{position:absolute;left:18px;top:253px;width:133px;height:230px;background:var(--teal);padding:9px 8px;color:#fff}
.intro-col h2{font-size:11px;font-weight:600;margin-bottom:6px}
.intro-col .body-text{font-size:5.5px}
.plan-ref{position:absolute;left:160px;top:226px;width:210px;text-align:center;font-size:12.5px}
.feature{position:absolute;width:100px;text-align:center}
.feature .icon{width:30px;height:30px;margin:0 auto}
.feature h3{font-size:5.6px;font-weight:600;color:var(--teal);margin:4px 0 2px}
.feature p{font-size:4.6px;line-height:1.35}

/* page 2 */
.type-band{position:absolute;left:0;top:0;width:370px;height:176px;background:var(--teal)}
.type-band h1{position:absolute;top:18px;width:100%;text-align:center;color:#fff;font-size:14px;font-weight:600}
.type-circle{position:absolute;top:54px;width:78px;height:78px;border-radius:50%;border:2.5px solid var(--orange)}
.type-circle--washers{left:27px;background:radial-gradient(circle at 55% 55%,#f7f7f7 0%,#f1a8a0 40%,#ec8078 100%)}
.type-circle--dishwashers{left:146px;background:radial-gradient(circle at 50% 55%,#c9cbce 0%,#eef0f1 55%,#fff 100%);display:flex;align-items:center;justify-content:center}
.type-circle--dishwashers span{font-size:6.4px;font-weight:600;color:var(--ink)}
.type-circle--fridges{left:265px;background:radial-gradient(circle at 45% 50%,#f2f4f6 0%,#a9d3f1 50%,#7dbde8 100%)}
.type-label{position:absolute;top:141px;width:120px;text-align:center;color:#fff;font-size:6.6px;font-weight:600}
.partner{position:absolute;top:166px;width:56px;height:23px;background:#fff;border:1px solid #e3e5e8;display:flex;align-items:center;justify-content:center;font-size:8px;font-weight:600;color:var(--orange)}
.photo-round{position:absolute;border-radius:50%;border:2.5px solid var(--orange)}

/* page 3 */
.booking-bar{position:absolute;left:0;top:0;width:370px;height:45px;background:var(--teal);border-bottom:2.5px solid var(--orange)}
.booking-bar h1{text-align:center;color:#fff;font-size:14px;font-weight:600;line-height:42px}
.step{position:absolute;top:62px;width:100px;text-align:center}
.step .icon{width:32px;height:32px;margin:0 auto}
.step h3{font-size:5.6px;font-weight:600;color:var(--teal);margin:4px 0 2px}
.step p{font-size:4.6px;line-height:1.35}
.terms-title{font-size:6px;font-weight:600;color:var(--teal)}
.terms-text{font-size:4.3px;line-height:1.4}
</style>
</head>
<body>

<!-- Page 1: Introduction / Repair Plan Ref -->
<section class="page page--intro">
  <svg class="hero-art" viewBox="0 0 370 260" aria-hidden="false">
    <defs>
      <linearGradient id="heroTone" x1="0" y1="0" x2="1" y2="1">
        <stop offset="0" stop-color="#5c5f66"/>
        <stop offset=".45" stop-color="#8e939b"/>
        <stop offset=".7" stop-color="#3b4f93"/>
        <stop offset="1" stop-color="#c9ccd1"/>
      </linearGradient>
    </defs>
    <polygon role="img" aria-label="Photo of a technician in blue overalls repairing a fridge freezer beside an open tool case" points="0,0 370,0 370,168 115,253 0,253" fill="url(#heroTone)"/>
    <polygon points="92,256 146,256 160,232 298,193 302,210 370,168 298,150 300,168 150,212" fill="var(--orange)"/>
  </svg>
  <div class="brand">
    <div class="brand-name">BIRCHWAY</div>
    <div class="brand-tag">APPLIANCE CARE</div>
  </div>

  <div class="intro-col">
    <h2>INTRODUCTION</h2>
    <div class="body-text">
      <p>Lorem ipsum dolor sit amet, consectetuer adipiscing elit, sed diam nonummy nibh euismod tincidunt ut laoreet dolore magna aliquam erat volutpat. Ut wisi enim ad minim veniam, quis nostrud exerci tation ullamcorper suscipit lobortis nisl ut aliquip ex ea commodo consequat. Duis autem vel eum iriure dolor in hendrerit in vulputate velit esse molestie consequat.</p>
      <p>vel illum dolore eu feugiat nulla facilisis at vero eros et accumsan et iusto odio dignissim qui blandit praesent luptatum zzril delenit augue duis dolore te feugait nulla facilisi.</p>
      <p>Lorem ipsum dolor sit amet, cons ectetuer adipiscing elit, sed diam nonummy nibh euismod tincidunt ut laoreet dolore magna aliquam erat volutpat.</p>
    </div>
  </div>

  <h2 class="plan-ref heading heading--teal">REPAIR PLAN REF</h2>

  <div class="feature" style="left:156px;top:262px">
    <svg class="icon" viewBox="0 0 30 30"><circle cx="15" cy="15" r="13" fill="none" stroke="var(--orange)" stroke-width="1.2"/><circle cx="15" cy="13" r="5" fill="none" stroke="var(--orange)" stroke-width="1.2"/><path d="M8 22h14" stroke="var(--orange)" stroke-width="1.2"/></svg>
    <h3>TECHNICAL SUPPORT</h3>
    <p>Tempor incididunt ut labore et dolore magna aliqua. Ut enim ad minim veniam, quis nostrud exercitation ullamco laboris nisi ut aliquip.</p>
  </div>
  <div class="feature" style="left:263px;top:262px">
    <svg class="icon" viewBox="0 0 30 30"><circle cx="15" cy="15" r="13" fill="none" stroke="var(--orange)" stroke-width="1.2"/><circle cx="15" cy="15" r="7" fill="none" stroke="var(--orange)" stroke-width="1.2"/><path d="M12 18l6-6" stroke="var(--orange)" stroke-width="1.6" stroke-linecap="round"/></svg>
    <h3>QUICK REPAIRS</h3>
    <p>Tempor incididunt ut labore et dolore magna aliqua. Ut enim ad minim veniam, quis nostrud exercitation ullamco laboris nisi ut aliquip.</p>
  </div>
  <div class="feature" style="left:190px;top:348px;width:140px">
    <svg class="icon" viewBox="0 0 30 30"><circle cx="15" cy="15" r="13" fill="none" stroke="var(--orange)" stroke-width="1.2"/><path d="M10 8h10v5a5 5 0 0 1-10 0z M15 18v4 M11 23h8" fill="none" stroke="var(--orange)" stroke-width="1.2"/></svg>
    <h3>COMPETITIVE PRICES</h3>
    <p>Tempor incididunt ut labore et dolore magna aliqua. Ut enim ad minim veniam, quis nostrud exercitation ullamco laboris nisi ut aliquip.</p>
  </div>

  <svg class="footer" viewBox="0 0 370 130"><polygon points="40,105 188,68 184,55 250,58 206,95 200,82 60,112" fill="var(--orange)"/><polygon points="0,130 0,118 60,112 200,82 206,95 370,52 370,130" fill="var(--dark)"/></svg>
  <div class="footer-photo" role="img" aria-label="Photo of a bright modern kitchen"></div>
  <div class="footer-contact"><p>123, Lorem ipsum dolor sit amet,<br>tetur adipiscing elit</p><p>Phone : +1 555 010 2040</p><p>Email : info@birchwaycare.com</p></div>
</section>

<!-- Page 2: Appliance Type / Cost / Payment Schedule -->
<section class="page page--appliances">
  <div class="type-band">
    <h1>APPLIANCE TYPE WE REPAIR</h1>
    <div class="type-circle type-circle--washers" role="img" aria-label="Photo of kitchen and laundry appliances on a pink backdrop"></div>
    <div class="type-circle type-circle--dishwashers" role="img" aria-label="Photo of a stainless dishwasher"><span>BOOK A REPAIR</span></div>
    <div class="type-circle type-circle--fridges" role="img" aria-label="Photo of an open dishwasher with dishes on a blue backdrop"></div>
    <div class="type-label" style="left:6px">WASHING MACHINES</div>
    <div class="type-label" style="left:125px">DISHWASHERS</div>
    <div class="type-label" style="left:244px">FRIDGE-FREEZERS</div>
  </div>
  <div class="partner" style="left:36px">Larkin</div>
  <div class="partner" style="left:117px">Halden</div>
  <div class="partner" style="left:198px">Brevik</div>
  <div class="partner" style="left:279px">Solvane</div>

  <h2 class="abs heading" style="left:14px;top:208px;font-size:10.8px;line-height:1.25"><span class="heading--teal">COST OF APPLIANCE WITHIN</span><br><span class="heading--orange">REPAIR PLAN</span></h2>
  <div class="abs body-text" style="left:14px;top:238px;width:220px">
    <p>Lorem ipsum dolor sit amet, consectetuer adipiscing elit, sed diam nonummy nibh euismod tincidunt ut laoreet dolore magna aliquam erat volutpat. Ut wisi enim ad minim veniam, quis nostrud exerci tation ullamcorper suscipit lobortis nisl ut aliquip ex ea commodo consequat. Duis autem vel eum iriure dolor in hendrerit in vulputate velit esse molestie consequat.</p>
    <p>vel illum dolore eu feugiat nulla facilisis at vero eros et accumsan et iusto odio dignissim qui blandit praesent luptatum zzril delenit augue duis dolore te feugait nulla facilisi.</p>
  </div>
  <div class="photo-round" role="img" aria-label="Photo of a technician in a cap repairing an appliance" style="left:244px;top:207px;width:112px;height:112px;background:linear-gradient(150deg,#dfe1e4 0%,#7c7f86 50%,#2f3440 100%)"></div>

  <div class="photo-round" role="img" aria-label="Photo of a technician fitting a kitchen cabinet" style="left:14px;top:327px;width:112px;height:112px;background:linear-gradient(150deg,#6a6d72 0%,#a0805d 55%,#d8c2a3 100%)"></div>
  <h2 class="abs heading heading--orange" style="left:139px;top:330px;font-size:11px">PAYMENT SCHEDULE</h2>
  <div class="abs body-text" style="left:139px;top:346px;width:220px">
    <p>Lorem ipsum dolor sit amet, consectetuer adipiscing elit, sed diam nonummy nibh euismod tincidunt ut laoreet dolore magna aliquam erat volutpat. Ut wisi enim ad minim veniam, quis nostrud exerci tation ullamcorper suscipit lobortis nisl ut aliquip ex ea commodo consequat. Duis autem vel eum iriure dolor in hendrerit in vulputate velit esse molestie consequat.</p>
    <p>vel illum dolore eu feugiat nulla facilisis at vero eros et accumsan et iusto odio dignissim qui blandit praesent luptatum zzril delenit augue duis dolore te feugait nulla facilisi.</p>
  </div>

  <svg class="footer" viewBox="0 0 370 130"><polygon points="40,105 188,68 184,55 250,58 206,95 200,82 60,112" fill="var(--orange)"/><polygon points="0,130 0,118 60,112 200,82 206,95 370,52 370,130" fill="var(--dark)"/></svg>
  <div class="footer-photo" role="img" aria-label="Photo of a bright modern kitchen"></div>
  <div class="footer-contact"><p>123, Lorem ipsum dolor sit amet,<br>tetur adipiscing elit</p><p>Phone : +1 555 010 2040</p><p>Email : info@birchwaycare.com</p></div>
</section>

<!-- Page 3: Booking process / Payment Dates / Terms -->
<section class="page page--booking">
  <div class="booking-bar"><h1>SIMPLE BOOKING PROCESS</h1></div>

  <div class="step" style="left:15px">
    <svg class="icon" viewBox="0 0 32 32"><circle cx="16" cy="16" r="14" fill="none" stroke="var(--orange)" stroke-width="1.2"/><circle cx="16" cy="13" r="5" fill="none" stroke="var(--teal)" stroke-width="1.2"/><path d="M9 24c1-4 4-6 7-6s6 2 7 6" fill="none" stroke="var(--teal)" stroke-width="1.2"/></svg>
    <h3>STEP 01</h3>
    <p>Tempor incididunt ut labore et dolore magna aliqua. Ut enim ad minim veniam, quis nostrud exercitation ullamco laboris nisi ut aliquip.</p>
  </div>
  <div class="step" style="left:135px">
    <svg class="icon" viewBox="0 0 32 32"><circle cx="16" cy="16" r="14" fill="none" stroke="var(--orange)" stroke-width="1.2"/><rect x="10" y="9" width="12" height="11" fill="none" stroke="var(--teal)" stroke-width="1.2"/><path d="M10 13h12 M8 24h16" stroke="var(--teal)" stroke-width="1.2"/></svg>
    <h3>STEP 02</h3>
    <p>Tempor incididunt ut labore et dolore magna aliqua. Ut enim ad minim veniam, quis nostrud exercitation ullamco laboris nisi ut aliquip.</p>
  </div>
  <div class="step" style="left:254px">
    <svg class="icon" viewBox="0 0 32 32"><circle cx="16" cy="16" r="14" fill="none" stroke="var(--orange)" stroke-width="1.2"/><circle cx="16" cy="12" r="4" fill="none" stroke="var(--teal)" stroke-width="1.2"/><path d="M10 24v-4h12v4 M22 9l3-3" fill="none" stroke="var(--teal)" stroke-width="1.2"/></svg>
    <h3>STEP 03</h3>
    <p>Tempor incididunt ut labore et dolore magna aliqua. Ut enim ad minim veniam, quis nostrud exercitation ullamco laboris nisi ut aliquip.</p>
  </div>

  <h2 class="abs heading heading--orange" style="left:19px;top:168px;font-size:11px">PAYMENT DATES</h2>
  <div class="abs body-text" style="left:19px;top:185px;width:218px">
    <p>Lorem ipsum dolor sit amet, consectetuer adipiscing elit, sed diam nonummy nibh euismod tincidunt ut laoreet dolore magna aliquam erat volutpat. Ut wisi enim ad minim veniam, quis nostrud exerci tation ullamcorper suscipit lobortis nisl ut aliquip ex ea commodo consequat. Duis autem vel eum iriure dolor in hendrerit in vulputate velit esse molestie consequat.</p>
  </div>
  <div class="photo-round" role="img" aria-label="Photo of an open-plan kitchen and dining room" style="left:261px;top:158px;width:90px;height:90px;background:linear-gradient(160deg,#f2f1ee 0%,#b9b3aa 55%,#6e6760 100%)"></div>

  <div class="photo-round" role="img" aria-label="Photo of a woman relaxing on a sofa" style="left:19px;top:270px;width:90px;height:90px;background:linear-gradient(160deg,#f4f2ee 0%,#d8c8b4 55%,#7f93b4 100%)"></div>
  <h2 class="abs heading heading--orange" style="left:132px;top:280px;font-size:11px">PAYMENT DATES</h2>
  <div class="abs body-text" style="left:132px;top:297px;width:220px">
    <p>Lorem ipsum dolor sit amet, consectetuer adipiscing elit, sed diam nonummy nibh euismod tincidunt ut laoreet dolore magna aliquam erat volutpat. Ut wisi enim ad minim veniam, quis nostrud exerci tation ullamcorper suscipit lobortis nisl ut aliquip ex ea commodo consequat. Duis autem vel eum iriure dolor in hendrerit in vulputate velit esse molestie consequat.</p>
  </div>

  <div class="abs" style="left:14px;top:374px;width:342px">
    <div class="terms-title">TERMS &amp; CONDITIONS</div>
    <p class="terms-text" style="margin-top:5px">Lorem ipsum dolor sit amet, consectetuer adipiscing elit, sed diam nonummy nibh euismod tincidunt ut laoreet dolore magna aliquam erat volutpat. Ut wisi enim ad minim veniam, quis nostrud exerci tation ullamcorper suscipit lobortis nisl ut aliquip ex ea commodo consequat. Duis autem vel eum iriure dolor in hendrerit in vulputate velit esse molestie consequat.</p>
    <p class="terms-text" style="margin-top:5px">vel illum dolore eu feugiat nulla facilisis at vero eros et accumsan et iusto odio dignissim qui blandit praesent luptatum zzril delenit augue duis dolore te feugait nulla facilisi.</p>
  </div>

  <svg class="footer" viewBox="0 0 370 130"><polygon points="40,105 188,68 184,55 250,58 206,95 200,82 60,112" fill="var(--orange)"/><polygon points="0,130 0,118 60,112 200,82 206,95 370,52 370,130" fill="var(--dark)"/></svg>
  <div class="footer-photo" role="img" aria-label="Photo of a bright modern kitchen"></div>
  <div class="footer-contact"><p>123, Lorem ipsum dolor sit amet,<br>tetur adipiscing elit</p><p>Phone : +1 555 010 2040</p><p>Email : info@birchwaycare.com</p></div>
</section>

</body>
</html>
```